Need a book cover design for a Lumora Book on Herbal Remedies

I need a book cover for my new ebook, here are the details:
Title: Meadow Cures
Sub-Heading: Buried Ancient Garden Tonics
Reclaiming the Wisdom of Roots for Everyday Wellness and Strength
Author: Nora Belcourt

```html
<!DOCTYPE html>
<html lang="en">
<head>
<meta charset="utf-8">
<title>Meadow Cures — Nora Belcourt</title>
<link rel="stylesheet" href="https://fonts.googleapis.com/css2?family=Crimson+Pro:ital,wght@0,400;0,500;1,400;1,500&display=swap">
<style>
  :root {
    --backdrop: #e4e4e4;
    --paper: #f7f7f6;
    --gold: #b3862a;
    --ink: #141414;
    --on-gold: #ffffff;
    --herb-light: #e6d3b3;
    --herb-mid: #c9a56e;
    --herb-dark: #8a6a3e;
  }
  * { box-sizing: border-box; margin: 0; padding: 0; }
  html, body {
    width: 1200px;
    height: 1200px;
    overflow: hidden;
    background: var(--backdrop);
  }
  .cover {
    position: absolute;
    left: 220px;
    top: 30px;
    width: 760px;
    height: 1140px;
    background: var(--paper);
    box-shadow: 0 6px 24px rgba(0,0,0,0.12);
    font-family: "Crimson Pro", Georgia, serif;
    text-align: center;
  }
  .cover__title {
    position: absolute;
    top: 70px;
    left: 0;
    width: 100%;
    color: var(--gold);
    font-weight: 500;
    font-size: 150px;
    line-height: 128px;
    letter-spacing: 2px;
    text-transform: uppercase;
  }
  .cover__band {
    position: absolute;
    top: 352px;
    left: 130px;
    width: 500px;
    height: 60px;
    background: var(--gold);
    color: var(--on-gold);
    font-style: italic;
    font-weight: 500;
    font-size: 34px;
    line-height: 60px;
  }
  .cover__tagline {
    position: absolute;
    top: 430px;
    left: 90px;
    width: 580px;
    color: var(--ink);
    font-style: italic;
    font-size: 28px;
    line-height: 34px;
  }
  .cover__art {
    position: absolute;
    top: 560px;
    left: 110px;
    width: 540px;
    height: 360px;
  }
  .cover__author {
    position: absolute;
    top: 990px;
    left: 0;
    width: 100%;
    color: var(--ink);
    font-size: 52px;
    font-weight: 400;
  }
</style>
</head>
<body>
  <main class="cover">
    <h1 class="cover__title">Meadow<br>Cures</h1>
    <p class="cover__band">Buried Ancient Garden Tonics</p>
    <p class="cover__tagline">Reclaiming the Wisdom of Roots for Everyday Wellness and Strength</p>
    <svg class="cover__art" viewBox="0 0 540 360" role="img" aria-label="Photograph of dried herbs, roots, leaves, flowers and a pine cone arranged in a row">
      <defs>
        <radialGradient id="herbGlow" cx="50%" cy="70%" r="60%">
          <stop offset="0%" stop-color="var(--herb-mid)"/>
          <stop offset="60%" stop-color="var(--herb-light)"/>
          <stop offset="100%" stop-color="var(--paper)"/>
        </radialGradient>
      </defs>
      <rect width="540" height="360" fill="url(#herbGlow)"/>
    </svg>
    <p class="cover__author">Nora Belcourt</p>
  </main>
</body>
</html>
```